Business cards Dorn Kelterhof GmbH & Co.KG

We need a uniform business card design template for our employees.
A template should be created to have the same design for all business cards.

Contact Information for Business Card

Firma und Firmierung, Name, Funktion in Unternehmen, Anschrift, Tel. Handynummer, Emailadresse, Internetseite

Colors

Designer to choose colors to be used in the design.

Requirements
Must have
• Our company logo must be on it

```html
<!DOCTYPE html>
<html lang="de">
<head>
<meta charset="utf-8">
<title>Dorn Kelterhof – Visitenkarten</title>
<link rel="stylesheet" href="https://fonts.googleapis.com/css2?family=Lora:wght@600;700&family=Mulish:wght@400;600&display=swap">
<style>
  :root {
    --backdrop: #2a2d31;
    --card: #151515;
    --pink: #e0577c;
    --lilac: #b894c8;
    --white: #f2f2f2;
    --serif: "Lora", Georgia, serif;
    --sans: "Mulish", Arial, sans-serif;
  }
  * { box-sizing: border-box; margin: 0; padding: 0; }
  html, body { width: 1200px; height: 900px; overflow: hidden; }
  body {
    background: var(--backdrop);
    display: flex;
    flex-direction: column;
    align-items: center;
    justify-content: center;
    gap: 60px;
  }
  .card {
    position: relative;
    width: 660px;
    height: 378px;
    background: var(--card);
    border-radius: 4px;
    box-shadow: 0 18px 40px rgba(0,0,0,0.45);
    overflow: hidden;
  }
  .brand-name {
    font-family: var(--serif);
    font-weight: 700;
    color: var(--pink);
    letter-spacing: 0.04em;
    text-transform: uppercase;
    line-height: 1.1;
  }

  /* Front */
  .card-front .brand-name {
    position: absolute;
    left: 0; right: 0;
    top: 138px;
    text-align: center;
    font-size: 44px;
  }
  .focus-list {
    position: absolute;
    left: 0; right: 0;
    bottom: 44px;
    display: flex;
    justify-content: center;
    gap: 16px;
    list-style: none;
    font-family: var(--sans);
    font-size: 14px;
    color: var(--white);
    text-transform: uppercase;
    letter-spacing: 0.02em;
  }
  .focus-list li::before {
    content: "";
    display: inline-block;
    width: 7px; height: 7px;
    margin-right: 6px;
    border-radius: 50%;
    background: var(--pink);
    vertical-align: 2px;
  }

  /* Back */
  .card-back .brand-name {
    position: absolute;
    left: 48px;
    top: 48px;
    font-size: 28px;
  }
  .contact-block {
    position: absolute;
    left: 300px;
    top: 132px;
    font-family: var(--sans);
  }
  .person-name {
    font-family: var(--serif);
    font-weight: 700;
    font-size: 24px;
    color: var(--pink);
    letter-spacing: 0.03em;
    text-transform: uppercase;
  }
  .person-role {
    font-size: 17px;
    color: var(--lilac);
    margin-bottom: 18px;
  }
  .contact-list { list-style: none; }
  .contact-list li {
    display: flex;
    align-items: center;
    gap: 10px;
    font-size: 17px;
    color: var(--lilac);
    line-height: 1.55;
  }
  .contact-list svg { width: 16px; height: 16px; flex: none; }
  .address {
    margin-top: 16px;
    font-size: 17px;
    color: var(--lilac);
    line-height: 1.45;
    font-style: normal;
  }
  .company {
    margin-top: 4px;
    font-family: var(--serif);
    font-weight: 700;
    font-size: 16px;
    color: var(--pink);
    text-transform: uppercase;
  }
  .accent-dash {
    position: absolute;
    left: 272px;
    top: 332px;
    width: 14px;
    height: 3px;
    background: var(--pink);
  }
</style>
</head>
<body>

  <section class="card card-front" aria-label="Vorderseite">
    <p class="brand-name">Dorn Kelterhof</p>
    <ul class="focus-list">
      <li>Lack of confidence</li>
      <li>Conflicting emotions</li>
      <li>No energy</li>
      <li>Phobias</li>
    </ul>
  </section>

  <section class="card card-back" aria-label="Rückseite">
    <p class="brand-name">Dorn Kelterhof</p>
    <div class="contact-block">
      <h1 class="person-name">Lena Harbeck</h1>
      <p class="person-role">Sales Manager</p>
      <ul class="contact-list">
        <li>
          <svg viewBox="0 0 16 16" fill="none" stroke="var(--pink)" stroke-width="1.4">
            <circle cx="8" cy="8" r="7"/>
            <path d="M5.5 4.5l1.5 1.6-.9 1.1c.6 1.2 1.4 2 2.6 2.6l1.1-.9 1.6 1.5-.9 1.1c-2.9-.4-5.3-2.8-5.9-5.9z" fill="var(--pink)" stroke="none"/>
          </svg>
          604-555-0142
        </li>
        <li>
          <svg viewBox="0 0 16 16" fill="none" stroke="var(--pink)" stroke-width="1.4">
            <rect x="1.5" y="3.5" width="13" height="9" rx="1"/>
            <path d="M1.5 4l6.5 5 6.5-5"/>
          </svg>
          info@dornkelterhof.com
        </li>
        <li>
          <svg viewBox="0 0 16 16" fill="none" stroke="var(--pink)" stroke-width="1.3">
            <circle cx="8" cy="8" r="6.5"/>
            <ellipse cx="8" cy="8" rx="3" ry="6.5"/>
            <path d="M1.5 8h13M2.5 5h11M2.5 11h11"/>
          </svg>
          www.dornkelterhof.com
        </li>
      </ul>
      <address class="address">PO Box 318, Elmsworth<br>Qld 4712</address>
      <p class="company">GmbH &amp; Co.KG</p>
    </div>
    <span class="accent-dash"></span>
  </section>

</body>
</html>
```